WWW.TRESSALO.IT BUSINNES CARD

WE NEED A BUSINESS CARD . I HAVE A COMPANY IN ITALY NR 1 IN HAIR MEDICAL CARE AN HAIR REPLECEMENT . IN CARD I NEED WRITE WEB ADDRESS, MAIL , ADDRESS, TELEPHONE NUMBER , AND NAME
IN THE BACK SIDE I NEED MY DOCTOR LOGO .
MY WEB SITE IS WWW.TRESSALO.IT
Updates

Hai bisogno di giorni extra per la revisione

Target Market(s)

CONSUMER B2C

Industry/Entity Type

Hair And Beauty

Contact Information for Business Card

I WANT A MEDICAL BUSINESS CARD.

Font styles to use
Other font styles liked:
• VERDANA

Colors
33a6d7
3176b5
85abd2
aedbee
eaf1f7
ffffff

Requirements
Must have
• I NEED MY LOGO AND LOGO OF DR TRESSALO

```html
<!DOCTYPE html>
<html lang="it">
<head>
<meta charset="utf-8">
<title>Tressalo – Biglietto da visita</title>
<link href="https://fonts.googleapis.com/css2?family=Montserrat:wght@400;500;800&display=swap" rel="stylesheet">
<style>
  :root {
    --sky: #33a6d7;
    --blue: #3176b5;
    --navy: #1b4f8f;
    --mist: #aedbee;
    --paper: #ffffff;
    --backdrop: #e4e8ec;
    --tone-warm: #e9d6c8;
    --tone-soft: #f3ebe4;
  }
  * { box-sizing: border-box; margin: 0; padding: 0; }
  html, body { width: 1200px; height: 1200px; overflow: hidden; }
  body {
    background: var(--backdrop);
    font-family: "Montserrat", Verdana, sans-serif;
    position: relative;
  }
  .card {
    position: absolute;
    left: 120px;
    width: 960px;
    height: 520px;
    background: var(--paper);
    box-shadow: 0 6px 24px rgba(0,0,0,0.12);
  }
  .card--back { top: 60px; }
  .card--front { top: 620px; }

  .mascot-area {
    position: absolute;
    left: 100px;
    top: 100px;
    width: 250px;
    height: 320px;
    background: linear-gradient(180deg, var(--tone-soft), var(--tone-warm));
  }

  .brand { position: absolute; }
  .brand__row { display: flex; align-items: center; gap: 14px; }
  .brand__dot {
    width: 46px; height: 46px;
    background: var(--sky);
    border-radius: 50%;
  }
  .brand__name {
    font-weight: 800;
    font-size: 72px;
    letter-spacing: 1px;
    color: var(--navy);
    line-height: 1;
  }
  .brand__tag {
    margin-top: 10px;
    margin-left: 60px;
    font-size: 17px;
    font-weight: 500;
    letter-spacing: 1px;
    color: var(--blue);
  }
  .card--back .brand { left: 420px; top: 185px; }
  .card--front .brand { left: 70px; top: 90px; }
  .card--front .brand__name { font-size: 64px; }

  .rule {
    position: absolute;
    left: 70px;
    top: 318px;
    width: 660px;
    height: 2px;
    background: var(--navy);
  }
  .person { position: absolute; right: 70px; top: 262px; text-align: right; }
  .person__name { font-size: 30px; font-weight: 500; color: var(--sky); }
  .person__role { font-size: 17px; color: var(--navy); margin-top: 4px; }
  .address {
    position: absolute; right: 70px; top: 340px;
    text-align: right; font-size: 19px; line-height: 1.3; color: var(--navy);
  }
  .contacts {
    position: absolute; left: 80px; top: 345px;
    list-style: none; font-size: 19px; color: var(--navy);
  }
  .contacts li { display: flex; align-items: center; gap: 18px; height: 34px; }
  .contacts svg { width: 18px; height: 18px; fill: var(--sky); flex: none; }
</style>
</head>
<body>
  <section class="card card--back" aria-label="Retro del biglietto">
    <div class="mascot-area" role="img" aria-label="Spazio per la mascotte del dottor Tressalo"></div>
    <div class="brand">
      <div class="brand__row"><span class="brand__dot"></span><span class="brand__name">TRESSALO</span></div>
      <div class="brand__tag">CURA E REINTEGRAZIONE DEI CAPELLI</div>
    </div>
  </section>

  <section class="card card--front" aria-label="Fronte del biglietto">
    <div class="brand">
      <div class="brand__row"><span class="brand__dot"></span><span class="brand__name">TRESSALO</span></div>
      <div class="brand__tag">CURA E REINTEGRAZIONE DEI CAPELLI</div>
    </div>
    <div class="person">
      <div class="person__name">Marco Bellini</div>
      <div class="person__role">Manager</div>
    </div>
    <div class="rule"></div>
    <div class="address">Via Fiorenza 12,<br>Parma 43121, Italia</div>
    <ul class="contacts">
      <li><svg viewBox="0 0 24 24"><path d="M6.6 10.8a15 15 0 0 0 6.6 6.6l2.2-2.2a1 1 0 0 1 1-.25 11.4 11.4 0 0 0 3.6.57 1 1 0 0 1 1 1V20a1 1 0 0 1-1 1A17 17 0 0 1 3 4a1 1 0 0 1 1-1h3.5a1 1 0 0 1 1 1c0 1.25.2 2.45.57 3.57a1 1 0 0 1-.25 1z"/></svg>0521-448-9073</li>
      <li><svg viewBox="0 0 24 24"><path d="M2 5h20v14H2zm2 2v.5l8 5 8-5V7l-8 5z"/></svg>info@tressalo.it</li>
      <li><svg viewBox="0 0 24 24"><path d="M12 2a10 10 0 1 0 0 20 10 10 0 0 0 0-20zm6.9 6h-3a15 15 0 0 0-1.3-3.9A8 8 0 0 1 18.9 8zM12 4c.8 1.2 1.5 2.5 1.9 4h-3.8c.4-1.5 1.1-2.8 1.9-4zM4.3 14a8 8 0 0 1 0-4h3.4a16 16 0 0 0 0 4zm.8 2h3a15 15 0 0 0 1.3 3.9A8 8 0 0 1 5.1 16zm3-8h-3a8 8 0 0 1 4.3-3.9A15 15 0 0 0 8.1 8zM12 20c-.8-1.2-1.5-2.5-1.9-4h3.8c-.4 1.5-1.1 2.8-1.9 4zm2.3-6H9.7a14 14 0 0 1 0-4h4.6a14 14 0 0 1 0 4zm.3 5.9a15 15 0 0 0 1.3-3.9h3a8 8 0 0 1-4.3 3.9zm1.7-5.9a16 16 0 0 0 0-4h3.4a8 8 0 0 1 0 4z"/></svg>www.tressalo.it</li>
    </ul>
  </section>
</body>
</html>
```